Design an App that allows to send money through messages

We need a design for an app that will be a text message app that allows you to send money in the messages.

This app is ChatterBox and CoinPouch infused into one app
CoinPouch - https://vidbay.example/k7QpRtZ2mWx

It also is a Crypto wallet, trade, buy, sell, swap, etc. I have attached a similar 'app' design however it needs to have it's own colour scheme.

Design an app similar to ChatterBox/Parleyo that allows to communicate with your contacts but also a Crypto wallet. In the actual messages users will be able to send Crypto tokens to each other - similar to qText Pear Pay (attached).

Design buttons, fields, wallet, and everything in the attached diagram of the other app.

These pages must be designed for the app:
- Login page (Login with phone number, pear ID)
- Main chats page (with all your messages with contacts)
- Actual messages (with the send money feature in a message - like pear pay)
- Crypto Wallet(s) with all tokens and assets
- Crypto Wallet import / new wallet page
- Buy/Sell Crypto token
- Markets page (shows all tokens - tokenboardly.com)
- Send/Receive pop-up
- Chart page of markets
- All transactions page
- Contacts page (from phone)
- Settings page (similar to chatterbox)

How payments will be made (via message):
https://vidbay.example/b3NfLxQ8sYe?t=77

Ideally design in Figma or other app for developers to understand which page is connected to which button.

Here is some inspiration on redesign chatterbox design app:
https://www.pinvault.example/pin/482716093527164839/

Winner who does all pages with the proper theme will receive an extra tip.

Payments through Messages and Cryptocurrency Buy/Sell/Trade/Swap/Send/Receive

Other font styles liked:
• Montserrat (or ANY font of your choosing)

• All App pages with Wireframe (Figma or Adobe XD)
• Creative designs throughout pages of app. Not your typical app.

```html
<!DOCTYPE html>
<html lang="en">
<head>
<meta charset="utf-8">
<title>Ravlo Coin – App Screens</title>
<link href="https://fonts.googleapis.com/css2?family=Urbanist:wght@400;500;600;700&display=swap" rel="stylesheet">
<style>
:root{
  --board:#2b2e3c;
  --screen:#15191b;
  --screen-deep:#101315;
  --header:#181c1f;
  --accent:#00efd6;
  --accent-ring:#6fa88a;
  --bubble:#2c4641;
  --text:#ffffff;
  --muted:#858b8f;
  --line:#262b2e;
  --title:#9fd4d6;
  --up:#2fd38e;
  --down:#f0445a;
}
*{box-sizing:border-box;margin:0;padding:0}
html,body{width:706px;height:1200px;overflow:hidden}
body{font-family:"Urbanist",sans-serif;color:var(--text);background:var(--board)}
.board{position:relative;width:706px;height:1200px;overflow:hidden;
  background:
   radial-gradient(circle at 245px 75px,rgba(226,128,120,.75),transparent 110px),
   radial-gradient(circle at 660px 30px,rgba(196,80,160,.6),transparent 110px),
   radial-gradient(circle at 80px 140px,rgba(40,110,180,.55),transparent 130px),
   radial-gradient(circle at 370px 320px,rgba(14,170,215,.9),transparent 90px),
   radial-gradient(circle at 370px 900px,rgba(20,185,220,.85),transparent 160px),
   radial-gradient(circle at 700px 900px,rgba(20,170,210,.6),transparent 130px),
   radial-gradient(circle at 640px 1100px,rgba(220,120,120,.6),transparent 130px),
   radial-gradient(circle at 60px 1100px,rgba(140,70,110,.5),transparent 140px),
   radial-gradient(circle at 380px 1210px,rgba(70,110,190,.6),transparent 140px),
   var(--board)}
.abs{position:absolute}
.section-title{position:absolute;font-size:13px;font-weight:500;color:var(--title);letter-spacing:.1px;white-space:nowrap}
.phone{position:absolute;width:210px;height:453px;border-radius:20px;overflow:hidden;
  background:linear-gradient(180deg,var(--header) 0%,var(--screen) 40%,var(--screen-deep) 100%)}
.status-time{position:absolute;left:13px;top:15px;font-size:7px;font-weight:600}
.status-icons{position:absolute;right:12px;top:16px}
.screen-head{position:absolute;left:0;top:0;width:100%;height:63px;background:var(--header)}
.screen-title{position:absolute;left:13px;top:39px;font-size:11px;font-weight:700;white-space:nowrap}
.icon{position:absolute}
.brand-ring{position:absolute;left:65px;top:73px;width:88px;height:88px;border-radius:50%;border:4px solid var(--accent-ring);box-shadow:0 0 10px rgba(111,168,138,.5)}
.brand-name{position:absolute;left:0;width:100%;top:168px;text-align:center;font-size:17px;font-weight:700}
.signin-label{position:absolute;left:22px;top:226px;font-size:7px;font-weight:700}
.field{position:absolute;left:22px;top:253px;width:166px;height:13px;border-bottom:1px solid #3a4144;font-size:5.5px;color:var(--muted)}
.remember{position:absolute;left:22px;top:275px;font-size:6px;color:#c9cdcf;display:flex;align-items:center;gap:4px}
.check{width:7px;height:7px;border-radius:1.5px;background:var(--accent);display:flex;align-items:center;justify-content:center}
.trouble{position:absolute;right:19px;top:275px;font-size:6px;font-weight:600;color:var(--accent)}
.btn-primary{position:absolute;background:var(--accent);color:#0d1a19;border-radius:3px;font-weight:600;display:flex;align-items:center;justify-content:center;gap:4px}
.btn-outline{position:absolute;border:1px solid var(--accent);color:var(--accent);border-radius:3px;font-weight:600;display:flex;align-items:center;justify-content:center;gap:4px}
.divider-or{position:absolute;left:21px;top:336px;width:167px;display:flex;align-items:center;gap:6px;font-size:5px;color:#666c70}
.divider-or span{flex:1;height:1px;background:#353b3e}
.signup{position:absolute;left:0;width:100%;top:424px;text-align:center;font-size:4.6px;color:var(--muted)}
.signup b{color:var(--accent);font-weight:600}
.chat-row{position:absolute;left:0;width:210px;height:32px}
.avatar{position:absolute;border-radius:50%;background:radial-gradient(circle at 50% 40%,#d9b9a0,#7d6a5e 70%,#3a3a3a)}
.avatar.grey{background:radial-gradient(circle at 50% 40%,#d6d6d6,#7a7a7a 70%,#3a3a3a)}
.avatar.warm{background:radial-gradient(circle at 50% 40%,#e2c2aa,#8a5d48 70%,#3d3430)}
.chat-row .avatar{left:13px;top:6px;width:20px;height:20px}
.chat-name{position:absolute;left:39px;top:8px;font-size:6px;font-weight:700;white-space:nowrap}
.chat-preview{position:absolute;left:39px;top:17px;font-size:5.5px;color:var(--muted);white-space:nowrap}
.chat-time{position:absolute;right:12px;top:19px;font-size:4.5px;font-weight:600;color:#a2a8ab}
.badge{position:absolute;right:12px;top:5px;width:9px;height:9px;border-radius:50%;background:var(--accent);color:#0d1a19;font-size:5px;font-weight:700;display:flex;align-items:center;justify-content:center}
.chat-row::after{content:"";position:absolute;left:12px;right:12px;bottom:0;height:1px;background:var(--line)}
.nav-bar{position:absolute;left:12px;width:186px;height:37px;border-radius:9px;background:#14181a;border:1px solid #22282b}
.nav-pill{position:absolute;background:var(--accent);color:#0d1a19;border-radius:3px;font-size:6.5px;font-weight:600;display:flex;align-items:center;justify-content:center;gap:4px}
.convo-name{position:absolute;left:55px;top:36px;font-size:6.2px;font-weight:700;white-space:nowrap}
.convo-status{position:absolute;left:55px;top:45px;font-size:5.5px;color:#c8cccf}
.day-pill{position:absolute;left:80px;top:63px;width:40px;height:11px;border-radius:6px;background:#1e2326;font-size:4.8px;font-weight:600;display:flex;align-items:center;justify-content:center}
.bubble{position:absolute;background:var(--bubble);border-radius:9px;font-size:6.5px;display:flex;align-items:center;padding-left:10px;white-space:nowrap}
.msg-time{position:absolute;font-size:4.5px;font-weight:600;color:#9aa0a3}
.composer{position:absolute;left:12px;top:411px;width:137px;height:19px;border:1px solid #2b3134;border-radius:5px;font-size:5.5px;color:#5f666a}
.send-btn{position:absolute;top:411px;width:19px;height:19px;border-radius:4px;display:flex;align-items:center;justify-content:center}
.balance-card{position:absolute;left:12px;top:73px;width:185px;height:36px;border:1px solid #2a3033;border-radius:5px;background:#16191b}
.balance-label{position:absolute;left:10px;top:7px;font-size:6.5px;color:#c9cdcf}
.balance-value{position:absolute;left:10px;top:16px;font-size:12.5px;font-weight:400;color:var(--accent)}
.tabs{position:absolute;left:12px;top:151px;width:185px;height:16px;border:1px solid #22282b;display:flex;font-size:6px;font-weight:600}
.tabs div{display:flex;align-items:center;justify-content:center;border-right:1px solid #22282b}
.tabs div:last-child{border-right:none}
.asset-row{position:absolute;left:12px;width:185px;height:32px;border-bottom:1px solid var(--line)}
.coin-mark{position:absolute;left:1px;top:6px;width:20px;height:20px;border-radius:50%;background:#1c2224;border:1px solid #2d3538}
.coin-mark::after{content:"";position:absolute;left:4px;top:4px;width:10px;height:10px;border-radius:50%;border:1px solid var(--accent)}
.asset-sym{position:absolute;left:25px;top:7px;font-size:8px;font-weight:600}
.asset-name{position:absolute;left:25px;top:17px;font-size:6px;color:#c0c4c7}
.asset-amt{position:absolute;right:0;top:7px;font-size:8px;font-weight:600}
.asset-val{position:absolute;right:0;top:18px;font-size:5.5px;color:#b8bdc0;white-space:nowrap}
.up{color:var(--up)}.down{color:var(--down)}
</style>
</head>
<body>
<main class="board">

  <h2 class="section-title" style="left:142px;top:86px">Login Page</h2>
  <section class="phone" style="left:135px;top:110px">
    <div class="status-time">9:41</div>
    <svg class="status-icons" width="34" height="7" viewBox="0 0 34 7"><g fill="#fff"><rect x="0" y="4" width="1.4" height="2.5"/><rect x="2.2" y="3" width="1.4" height="3.5"/><rect x="4.4" y="1.8" width="1.4" height="4.7"/><rect x="6.6" y=".6" width="1.4" height="5.9"/><path d="M14 6.3l1.2-1.3a1.8 1.8 0 0 0-2.4 0z M11.5 3.9a3.6 3.6 0 0 1 5 0l-.8.8a2.5 2.5 0 0 0-3.4 0z M10.2 2.6a5.4 5.4 0 0 1 7.6 0l-.8.8a4.2 4.2 0 0 0-6 0z"/><rect x="22" y="1" width="10" height="5" rx="1.2"/><rect x="32.6" y="2.5" width=".9" height="2" rx=".4"/></g></svg>
    <div class="brand-ring" aria-hidden="true"></div>
    <div class="brand-name">Ravlo Coin</div>
    <div class="signin-label">Sign in to your account</div>
    <div class="field">Enter Your Phone Number</div>
    <div class="remember"><span class="check"><svg width="5" height="4" viewBox="0 0 5 4"><path d="M.6 2l1.3 1.3L4.4.6" stroke="#0d1a19" stroke-width=".9" fill="none"/></svg></span>Remeber me</div>
    <div class="trouble">Trouble login?</div>
    <div class="btn-primary" style="left:22px;top:304px;width:166px;height:21px;font-size:7px">Login</div>
    <div class="divider-or"><span></span>OR<span></span></div>
    <div class="btn-outline" style="left:22px;top:351px;width:166px;height:21px;font-size:7px">Sign in with Pear</div>
    <div class="signup">Don't have an account? <b>Signup here</b></div>
  </section>

  <h2 class="section-title" style="left:411px;top:86px">Main chats page</h2>
  <section class="phone" style="left:404px;top:109px">
    <div class="screen-head"></div>
    <div class="status-time">9:41</div>
    <svg class="status-icons" width="34" height="7" viewBox="0 0 34 7"><g fill="#fff"><rect x="0" y="4" width="1.4" height="2.5"/><rect x="2.2" y="3" width="1.4" height="3.5"/><rect x="4.4" y="1.8" width="1.4" height="4.7"/><rect x="6.6" y=".6" width="1.4" height="5.9"/><path d="M14 6.3l1.2-1.3a1.8 1.8 0 0 0-2.4 0z M11.5 3.9a3.6 3.6 0 0 1 5 0l-.8.8a2.5 2.5 0 0 0-3.4 0z M10.2 2.6a5.4 5.4 0 0 1 7.6 0l-.8.8a4.2 4.2 0 0 0-6 0z"/><rect x="22" y="1" width="10" height="5" rx="1.2"/><rect x="32.6" y="2.5" width=".9" height="2" rx=".4"/></g></svg>
    <div class="screen-title">Messages</div>
    <svg class="icon" style="left:172px;top:41px" width="11" height="11" viewBox="0 0 11 11"><circle cx="4.8" cy="4.8" r="3.8" stroke="#fff" stroke-width="1.1" fill="none"/><path d="M7.6 7.6l2.4 2.4" stroke="#fff" stroke-width="1.1" stroke-linecap="round"/></svg>
    <svg class="icon" style="left:194px;top:41px" width="3" height="11" viewBox="0 0 3 11"><g fill="#fff"><circle cx="1.5" cy="1.5" r="1.1"/><circle cx="1.5" cy="5.5" r="1.1"/><circle cx="1.5" cy="9.5" r="1.1"/></g></svg>

    <div class="chat-row" style="top:69px"><div class="avatar" role="img" aria-label="Contact photo of Jonah Ardley"></div><div class="chat-name">Jonah Ardley</div><div class="chat-preview">How are you?</div><div class="badge">2</div><div class="chat-time">08.34 PM</div></div>
    <div class="chat-row" style="top:101px"><div class="avatar grey" role="img" aria-label="Contact photo of Alec Sorrel"></div><div class="chat-name">Alec Sorrel</div><div class="chat-preview">Fine</div><div class="chat-time">08.34 PM</div></div>
    <div class="chat-row" style="top:133px"><div class="avatar warm" role="img" aria-label="Contact photo of Shona Jessup"></div><div class="chat-name">Shona Jessup</div><div class="chat-preview">When will you come?</div><div class="chat-time">08.34 PM</div></div>
    <div class="chat-row" style="top:165px"><div class="avatar" role="img" aria-label="Contact photo of Jonah Ardley"></div><div class="chat-name">Jonah Ardley</div><div class="chat-preview">How are you?</div><div class="badge">2</div><div class="chat-time">08.34 PM</div></div>
    <div class="chat-row" style="top:197px"><div class="avatar grey" role="img" aria-label="Contact photo of Alec Sorrel"></div><div class="chat-name">Alec Sorrel</div><div class="chat-preview">Fine</div><div class="chat-time">08.34 PM</div></div>
    <div class="chat-row" style="top:229px"><div class="avatar warm" role="img" aria-label="Contact photo of Shona Jessup"></div><div class="chat-name">Shona Jessup</div><div class="chat-preview">When will you come?</div><div class="chat-time">08.34 PM</div></div>
    <div class="chat-row" style="top:261px"><div class="avatar" role="img" aria-label="Contact photo of Jonah Ardley"></div><div class="chat-name">Jonah Ardley</div><div class="chat-preview">How are you?</div><div class="badge">2</div><div class="chat-time">08.34 PM</div></div>
    <div class="chat-row" style="top:293px"><div class="avatar grey" role="img" aria-label="Contact photo of Alec Sorrel"></div><div class="chat-name">Alec Sorrel</div><div class="chat-preview">Fine</div><div class="chat-time">08.34 PM</div></div>
    <div class="chat-row" style="top:325px"><div class="avatar warm" role="img" aria-label="Contact photo of Shona Jessup"></div><div class="chat-name">Shona Jessup</div><div class="chat-preview">When will you come?</div><div class="chat-time">08.34 PM</div></div>
    <div class="chat-row" style="top:357px"><div class="avatar" role="img" aria-label="Contact photo of Jonah Ardley"></div><div class="chat-name">Jonah Ardley</div><div class="chat-preview">How are you?</div><div class="badge">2</div><div class="chat-time">08.34 PM</div></div>

    <nav class="nav-bar" style="top:404px">
      <svg class="icon" style="left:14px;top:12px" width="12" height="12" viewBox="0 0 12 12"><rect x="1" y="2.5" width="10" height="8.5" rx="1.5" stroke="#8a9093" fill="none"/><path d="M1 5h10M2.5 2.5V1h7v1.5" stroke="#8a9093" fill="none"/></svg>
      <svg class="icon" style="left:41px;top:12px" width="12" height="12" viewBox="0 0 12 12"><path d="M1 4h10L8.5 1.5M11 8H1l2.5 2.5" stroke="#8a9093" fill="none" stroke-linecap="round" stroke-linejoin="round"/></svg>
      <div class="nav-pill" style="left:67px;top:8px;width:47px;height:20px"><svg width="11" height="10" viewBox="0 0 11 10"><path d="M1 1h9v6H4L1.5 9V7H1z" stroke="#0d1a19" fill="none" stroke-linejoin="round"/><g fill="#0d1a19"><circle cx="3.5" cy="4" r=".6"/><circle cx="5.5" cy="4" r=".6"/><circle cx="7.5" cy="4" r=".6"/></g></svg>Chats</div>
      <svg class="icon" style="left:128px;top:12px" width="12" height="12" viewBox="0 0 12 12"><path d="M1 1v10h10M3 8l3-3 2 2 3-3.5" stroke="#8a9093" fill="none" stroke-linejoin="round"/></svg>
      <svg class="icon" style="left:155px;top:12px" width="12" height="12" viewBox="0 0 12 12"><circle cx="6" cy="6" r="2" stroke="#8a9093" fill="none"/><path d="M6 .8l1.2 1.4 1.8-.3.5 1.7 1.7.6-.4 1.8L12 7l-1.5 1 .2 1.8-1.8.2-.9 1.6L6.4 11 4.8 11.8 3.9 10.2 2 10l.3-1.8L.8 7 2 5.7 1.6 4 3.3 3.4 3.8 1.7 5.5 2z" stroke="#8a9093" stroke-width=".8" fill="none" stroke-linejoin="round"/></svg>
    </nav>
  </section>

  <h2 class="section-title" style="left:142px;top:623px">Actual messages</h2>
  <section class="phone" style="left:135px;top:648px">
    <div class="screen-head" style="height:56px"></div>
    <div class="status-time">9:41</div>
    <svg class="status-icons" width="34" height="7" viewBox="0 0 34 7"><g fill="#fff"><rect x="0" y="4" width="1.4" height="2.5"/><rect x="2.2" y="3" width="1.4" height="3.5"/><rect x="4.4" y="1.8" width="1.4" height="4.7"/><rect x="6.6" y=".6" width="1.4" height="5.9"/><path d="M14 6.3l1.2-1.3a1.8 1.8 0 0 0-2.4 0z M11.5 3.9a3.6 3.6 0 0 1 5 0l-.8.8a2.5 2.5 0 0 0-3.4 0z M10.2 2.6a5.4 5.4 0 0 1 7.6 0l-.8.8a4.2 4.2 0 0 0-6 0z"/><rect x="22" y="1" width="10" height="5" rx="1.2"/><rect x="32.6" y="2.5" width=".9" height="2" rx=".4"/></g></svg>
    <svg class="icon" style="left:12px;top:38px" width="10" height="10" viewBox="0 0 10 10"><path d="M9 5H1.5M4.5 1.5L1 5l3.5 3.5" stroke="#fff" stroke-width="1.1" fill="none" stroke-linecap="round" stroke-linejoin="round"/></svg>
    <div class="avatar" style="left:30px;top:33px;width:20px;height:20px" role="img" aria-label="Contact photo of Jonah Ardley"></div>
    <div class="convo-name">Jonah Ardley</div>
    <div class="convo-status">Online</div>
    <svg class="icon" style="left:171px;top:37px" width="11" height="11" viewBox="0 0 11 11"><circle cx="4.8" cy="4.8" r="3.8" stroke="#fff" stroke-width="1.1" fill="none"/><path d="M7.6 7.6l2.4 2.4" stroke="#fff" stroke-width="1.1" stroke-linecap="round"/></svg>
    <svg class="icon" style="left:194px;top:37px" width="3" height="11" viewBox="0 0 3 11"><g fill="#fff"><circle cx="1.5" cy="1.5" r="1.1"/><circle cx="1.5" cy="5.5" r="1.1"/><circle cx="1.5" cy="9.5" r="1.1"/></g></svg>

    <div class="day-pill">Today</div>
    <div class="bubble" style="left:12px;top:80px;width:32px;height:18px">Hi!</div>
    <div class="msg-time" style="left:12px;top:102px">08.34 PM</div>
    <div class="bubble" style="left:120px;top:105px;width:77px;height:19px;padding-left:13px">Hi! How are you?</div>
    <div class="msg-time" style="right:13px;top:127px">08.35 PM</div>
    <div class="bubble" style="left:12px;top:134px;width:49px;height:18px">Fine</div>
    <div class="msg-time" style="left:12px;top:156px">08.40 PM</div>

    <div class="composer">
      <svg class="icon" style="left:5px;top:5px" width="8" height="8" viewBox="0 0 8 8"><circle cx="4" cy="4" r="3.4" stroke="#5f666a" stroke-width=".7" fill="none"/><path d="M2.6 4.8a1.7 1.7 0 0 0 2.8 0" stroke="#5f666a" stroke-width=".7" fill="none"/></svg>
      <span class="abs" style="left:22px;top:5.5px">Type a message.....</span>
      <svg class="icon" style="left:110px;top:5px" width="9" height="8" viewBox="0 0 9 8"><rect x=".5" y="1.8" width="8" height="5.7" rx="1" stroke="#5f666a" stroke-width=".7" fill="none"/><circle cx="4.5" cy="4.6" r="1.5" stroke="#5f666a" stroke-width=".7" fill="none"/></svg>
      <svg class="icon" style="left:125px;top:5px" width="8" height="8" viewBox="0 0 8 8"><path d="M6.8 3.6L4 6.4a1.8 1.8 0 0 1-2.6-2.6l3-3a1.2 1.2 0 0 1 1.7 1.7L3.2 5.4" stroke="#5f666a" stroke-width=".7" fill="none" stroke-linecap="round"/></svg>
    </div>
    <div class="send-btn" style="left:155px;background:var(--accent)"><svg width="11" height="10" viewBox="0 0 11 10"><path d="M1 1l9 4-9 4 1.5-4zM2.5 5H6" stroke="#0d1a19" stroke-width=".9" fill="none" stroke-linejoin="round"/></svg></div>
    <div class="send-btn" style="left:178px;border:1px solid var(--accent)"><span style="width:9px;height:9px;background:var(--accent);border-radius:1.5px" aria-hidden="true"></span></div>
  </section>

  <h2 class="section-title" style="left:411px;top:623px">Crypto Wallet(s)</h2>
  <section class="phone" style="left:404px;top:653px">
    <div class="screen-head"></div>
    <div class="status-time">9:41</div>
    <svg class="status-icons" width="34" height="7" viewBox="0 0 34 7"><g fill="#fff"><rect x="0" y="4" width="1.4" height="2.5"/><rect x="2.2" y="3" width="1.4" height="3.5"/><rect x="4.4" y="1.8" width="1.4" height="4.7"/><rect x="6.6" y=".6" width="1.4" height="5.9"/><path d="M14 6.3l1.2-1.3a1.8 1.8 0 0 0-2.4 0z M11.5 3.9a3.6 3.6 0 0 1 5 0l-.8.8a2.5 2.5 0 0 0-3.4 0z M10.2 2.6a5.4 5.4 0 0 1 7.6 0l-.8.8a4.2 4.2 0 0 0-6 0z"/><rect x="22" y="1" width="10" height="5" rx="1.2"/><rect x="32.6" y="2.5" width=".9" height="2" rx=".4"/></g></svg>
    <div class="screen-title">My Wallet</div>
    <svg class="icon" style="left:172px;top:41px" width="11" height="11" viewBox="0 0 11 11"><circle cx="4.8" cy="4.8" r="3.8" stroke="#fff" stroke-width="1.1" fill="none"/><path d="M7.6 7.6l2.4 2.4" stroke="#fff" stroke-width="1.1" stroke-linecap="round"/></svg>
    <svg class="icon" style="left:194px;top:41px" width="3" height="11" viewBox="0 0 3 11"><g fill="#fff"><circle cx="1.5" cy="1.5" r="1.1"/><circle cx="1.5" cy="5.5" r="1.1"/><circle cx="1.5" cy="9.5" r="1.1"/></g></svg>

    <div class="balance-card">
      <div class="balance-label">My balance</div>
      <div class="balance-value">$ 1,965.97</div>
      <svg class="icon" style="right:7px;top:6px" width="8" height="8" viewBox="0 0 12 12"><circle cx="6" cy="6" r="2" stroke="#8a9093" fill="none"/><path d="M6 .8l1.2 1.4 1.8-.3.5 1.7 1.7.6-.4 1.8L12 7l-1.5 1 .2 1.8-1.8.2-.9 1.6L6.4 11 4.8 11.8 3.9 10.2 2 10l.3-1.8L.8 7 2 5.7 1.6 4 3.3 3.4 3.8 1.7 5.5 2z" stroke="#8a9093" stroke-width=".8" fill="none"/></svg>
    </div>
    <div class="btn-primary" style="left:13px;top:122px;width:90px;height:21px;font-size:6.5px"><svg width="9" height="9" viewBox="0 0 9 9"><circle cx="4.5" cy="4.5" r="3.9" stroke="#0d1a19" stroke-width=".8" fill="none"/><path d="M4.5 6.5v-4M2.8 4.1l1.7-1.7 1.7 1.7" stroke="#0d1a19" stroke-width=".8" fill="none"/></svg>Buy</div>
    <div class="btn-outline" style="left:107px;top:122px;width:90px;height:21px;font-size:6.5px"><svg width="9" height="9" viewBox="0 0 9 9"><circle cx="4.5" cy="4.5" r="3.9" stroke="#00efd6" stroke-width=".8" fill="none"/><path d="M4.5 2.5v4M2.8 4.9l1.7 1.7 1.7-1.7" stroke="#00efd6" stroke-width=".8" fill="none"/></svg>Sell</div>
    <div class="tabs">
      <div style="width:22px"><svg width="8" height="8" viewBox="0 0 8 8"><path d="M4 .6l1 2.2 2.4.2-1.8 1.6.6 2.4L4 5.8 1.8 7l.6-2.4L.6 3l2.4-.2z" stroke="#8a9093" stroke-width=".6" fill="none" stroke-linejoin="round"/></svg></div>
      <div style="width:82px">Cryptocurrencies</div>
      <div style="flex:1">NFT</div>
    </div>
    <div class="asset-row" style="top:175px">
      <div class="coin-mark" aria-hidden="true"></div>
      <div class="asset-sym">BMT <span style="font-size:6px;color:#8a9093">☆</span></div>
      <div class="asset-name">Blockmint</div>
      <div class="asset-amt">0,237546743</div>
      <div class="asset-val">$ 17,310.30 <span class="up">(+2.13)</span></div>
    </div>
    <div class="asset-row" style="top:207px">
      <div class="coin-mark" aria-hidden="true"></div>
      <div class="asset-sym">ETN <span style="font-size:6px;color:#8a9093">☆</span></div>
      <div class="asset-name">Etheron</div>
      <div class="asset-amt">0,546743</div>
      <div class="asset-val">$ 1,277.50 <span class="down">(-3.16)</span></div>
    </div>

    <nav class="nav-bar" style="top:402px">
      <div class="nav-pill" style="left:8px;top:8px;width:47px;height:20px"><svg width="11" height="11" viewBox="0 0 12 12"><rect x="1" y="2.5" width="10" height="8.5" rx="1.5" stroke="#0d1a19" fill="none"/><path d="M1 5h10M2.5 2.5V1h7v1.5" stroke="#0d1a19" fill="none"/></svg>Wallet</div>
      <svg class="icon" style="left:68px;top:12px" width="12" height="12" viewBox="0 0 12 12"><path d="M1 4h10L8.5 1.5M11 8H1l2.5 2.5" stroke="#8a9093" fill="none" stroke-linecap="round" stroke-linejoin="round"/></svg>
      <svg class="icon" style="left:99px;top:12px" width="12" height="12" viewBox="0 0 11 10"><path d="M1 1h9v6H4L1.5 9V7H1z" stroke="#8a9093" fill="none" stroke-linejoin="round"/><g fill="#8a9093"><circle cx="3.5" cy="4" r=".6"/><circle cx="5.5" cy="4" r=".6"/><circle cx="7.5" cy="4" r=".6"/></g></svg>
      <svg class="icon" style="left:130px;top:12px" width="12" height="12" viewBox="0 0 12 12"><path d="M1 1v10h10M3 8l3-3 2 2 3-3.5" stroke="#8a9093" fill="none" stroke-linejoin="round"/></svg>
      <svg class="icon" style="left:160px;top:12px" width="12" height="12" viewBox="0 0 12 12"><circle cx="6" cy="6" r="2" stroke="#8a9093" fill="none"/><path d="M6 .8l1.2 1.4 1.8-.3.5 1.7 1.7.6-.4 1.8L12 7l-1.5 1 .2 1.8-1.8.2-.9 1.6L6.4 11 4.8 11.8 3.9 10.2 2 10l.3-1.8L.8 7 2 5.7 1.6 4 3.3 3.4 3.8 1.7 5.5 2z" stroke="#8a9093" stroke-width=".8" fill="none" stroke-linejoin="round"/></svg>
    </nav>
  </section>

</main>
</body>
</html>
```